Corporate Web Redesign Project - coded

We would like redesign/refresh of our current site that would allow us to increase the depth of content and create a high quality impression for visitors.

Current site - http://corvanisystems.com/

A previous web redesign project has improved our site but it has not really reached the level we require.

Our customers are global, blue chip, organisations and a professional, corporate style of site is required.

Please note we would prefer a coded website to a just a design. We are happy to provide a zip of our current site if required.
Updates

                                   

Target Market(s)

Global oil and gas producers, KR, Tamberline, Orvadex etc.

Industry/Entity Type

It Professional

Requirements
Must have
• Design should support the level of content we currently have in the existing sitemap - although it should be expandable a site design for a large / complex site would not be appropriate

All current content / pages to be reflected in design

Must be visually appealing

Intuitive and clear navigation that is expandable

Display a high level of professionalism

Use a consistent palette of colours that complements our logo

Clean and organized layout

A way to capture visitor’s information or Call to action (i.e. contact link or form) on every page

Prominent Contact Information
Should not have
• Flash

```html
<!DOCTYPE html>
<html lang="en">
<head>
<meta charset="utf-8">
<title>Corvani Systems</title>
<link href="https://fonts.googleapis.com/css2?family=Open+Sans:wght@400;600&family=PT+Sans:wght@400;700&display=swap" rel="stylesheet">
<style>
:root{
  --page:#e4e4e4;
  --panel:#f1f1f1;
  --panel-edge:#d2d2d2;
  --teal-dark:#123f43;
  --teal:#1c5a60;
  --teal-light:#6ab0b4;
  --slate:#4a4a4a;
  --text:#222;
  --muted:#777;
  --grey-band:#9a9a9a;
  --white:#fff;
}
*{box-sizing:border-box;margin:0;padding:0}
html,body{width:880px;height:1200px;overflow:hidden}
body{background:var(--page);font-family:Arial,Helvetica,sans-serif;color:var(--text);position:relative}
.band{position:absolute;left:94px;width:690px;height:5px;background:#bdbdbd}
.band.top{top:0}.band.bottom{top:1195px}
.abs{position:absolute}

.brand{left:94px;top:30px;display:flex;align-items:center;gap:10px}
.brand-mark{width:26px;height:26px;background:var(--teal)}
.brand-name{font-family:"PT Sans",sans-serif;font-weight:700;font-size:24px;color:var(--teal);letter-spacing:1px}
.enquiry{right:96px;top:36px;text-align:right;font-family:"Open Sans",sans-serif;font-size:12px;color:var(--slate);line-height:17px}
.enquiry a{color:var(--teal);text-decoration:none}

.nav{left:94px;top:100px;width:690px;height:31px;background:linear-gradient(#fbfbfb,#e3e3e3);border:1px solid #cfcfcf;box-shadow:0 2px 3px rgba(0,0,0,.12);display:flex}
.nav a{font-family:"Open Sans",sans-serif;font-size:12.5px;color:#999;text-decoration:none;padding:0 17px;line-height:29px;border-right:1px solid #d4d4d4}
.nav a.current{color:var(--teal-dark);background:linear-gradient(#eee,#d8d8d8)}

.card{background:var(--panel);border:1px solid var(--panel-edge);box-shadow:0 3px 5px rgba(0,0,0,.12)}
.slider{left:94px;top:156px;width:690px;height:235px}
.slide{position:absolute;left:10px;top:9px;width:669px;height:215px;background:linear-gradient(90deg,#8fd6dc 0%,#7cc2c7 45%,#65a9ad 100%)}
.slide-photo{position:absolute;left:0;top:0;width:360px;height:215px;background:linear-gradient(#8fd8de 0%,#9bd3d7 55%,#4d8fa4 78%,#2f6f89 100%)}
.slide-copy{position:absolute;left:300px;top:58px;color:var(--text)}
.slide-copy h1{font-family:"PT Sans",sans-serif;font-size:23px;font-weight:700;color:var(--white);margin-bottom:10px}
.slide-copy li{list-style:none;font-family:"Open Sans",sans-serif;font-size:12.5px;line-height:19px;padding-left:12px;position:relative}
.slide-copy li:before{content:"";position:absolute;left:0;top:7px;width:5px;height:5px;background:#111}
.dots{position:absolute;left:317px;top:203px;display:flex;gap:3px}
.dots span{width:6px;height:6px;background:var(--white)}
.arrow{top:265px}

.services{left:94px;top:422px;width:690px;height:221px}
.section-title{font-family:"Open Sans",sans-serif;font-size:20px;color:var(--teal-dark);text-align:center}
.services .section-title{margin-top:10px}
.tiles{position:absolute;left:8px;top:41px;display:flex;gap:1px}
.tile{width:168px;height:167px;position:relative;overflow:hidden}
.tile h3{font-family:"Open Sans",sans-serif;font-weight:400;font-size:14.5px;text-align:center;line-height:18px;position:relative;z-index:1}
.tile.time{background:#8c8c8c}
.tile.time h3{color:var(--white);padding-top:12px}
.tile .visual{position:absolute;left:0;right:0;bottom:0}
.tile.time .visual{top:60px;background:radial-gradient(circle at 50% 55%,#d9d9d9 0%,#9a9a9a 45%,#8c8c8c 70%)}
.read-more{position:absolute;left:14px;top:119px;width:137px;height:35px;background:var(--teal-dark);border:1px solid #d8d8d8;color:var(--white);font-family:"Open Sans",sans-serif;font-size:12.5px;text-align:center;line-height:33px;z-index:2}
.tile.dark{background:#1f2426}
.tile.dark h3{color:var(--teal-light);padding-top:12px;height:52px}
.tile.materials .visual{top:52px;background:radial-gradient(circle at 50% 45%,#8aa3ad 0%,#3d4a52 50%,#1b2226 100%)}
.tile.lessons h3{color:var(--teal-light);padding-top:19px;height:52px}
.tile.lessons .visual{top:52px;background:linear-gradient(135deg,#f2f2f2,#dcdcdc 60%,#c9b8a8)}
.tile.consult h3{padding-top:17px}
.tile.consult .visual{top:52px;background:linear-gradient(#8fb4cc,#6d98b4)}

.partners-title{left:94px;top:660px;width:690px}
.partners{left:105px;top:700px;width:670px;display:flex;justify-content:space-between;align-items:center}
.partners span{font-family:"Open Sans",sans-serif;font-size:12px;font-weight:600;color:#5a5a5a}

.info{left:94px;top:743px;width:690px;height:252px}
.info-inner{position:absolute;left:10px;top:10px;width:669px;height:230px;background:#f6f6f6}
.col{position:absolute;top:16px;width:180px;font-size:9px;line-height:12px;color:var(--text)}
.col h2{font-family:Arial,sans-serif;font-size:15px;color:#555;margin-bottom:12px}
.col p{margin-bottom:10px}
.col strong{display:block}
.col.about{left:17px;width:186px}
.col.news{left:246px;width:190px}
.col.location{left:474px}
.btn-more{position:absolute;top:196px;width:86px;height:22px;border:1px solid #c4c4c4;background:linear-gradient(#fdfdfd,#e7e7e7);font-size:8px;color:#777;text-align:center;line-height:20px;box-shadow:0 1px 2px rgba(0,0,0,.15)}

.partner-band{left:94px;top:1013px;width:330px;height:55px;background:var(--teal-dark);color:var(--white);text-align:center;padding-top:11px}
.partner-band b{display:block;font-family:"PT Sans",sans-serif;font-size:17px;font-weight:400}
.partner-band small{display:block;font-size:6.5px;margin-top:1px}
.touch-band{left:94px;top:1081px;width:330px;height:53px;background:var(--grey-band)}
.touch-pill{position:absolute;left:48px;top:9px;width:228px;height:34px;border:2px solid var(--white);border-radius:8px;display:flex;align-items:center;padding-left:10px;gap:12px;color:var(--white);font-family:"PT Sans",sans-serif;font-weight:700;font-size:19px}

.form-card{left:438px;top:1013px;width:346px;height:121px}
.form-inner{position:absolute;left:10px;top:10px;width:325px;height:100px;background:#f7f7f7}
.field{position:absolute;height:18px;border:1px solid #aaa;background:var(--white);font-size:8.5px;color:#444;padding:3px 5px}
.send{position:absolute;left:238px;top:63px;width:75px;height:27px;background:var(--teal-dark);color:var(--white);font-family:"Open Sans",sans-serif;font-weight:600;font-size:12px;text-align:center;line-height:27px}

.foot-nav{left:95px;top:1154px;font-size:9px;color:#222}
.foot-nav a{color:#222;text-decoration:none}
.foot-nav a.current{color:var(--teal)}
.copyright{left:95px;top:1170px;font-size:8.5px;color:#333}
.social{top:1154px;width:22px;height:22px;background:linear-gradient(#fdfdfd,#e2e2e2);border:1px solid #c9c9c9}
</style>
</head>
<body>
<div class="band top"></div>

<header>
  <div class="abs brand"><span class="brand-mark"></span><span class="brand-name">CORVANI SYSTEMS</span></div>
  <div class="abs enquiry">For general enquiries contact<br><a href="#">enquiries@corvanisystems.com</a></div>
  <nav class="abs nav">
    <a class="current" href="#">HOME</a><a href="#">NEWS</a><a href="#">ABOUT US</a><a href="#">SOLUTIONS</a><a href="#">CONTACT US</a>
  </nav>
</header>

<svg class="abs arrow" style="left:68px" width="12" height="16" viewBox="0 0 12 16"><path d="M10 2 4 8l6 6" fill="none" stroke="#1c4a70" stroke-width="3"/></svg>
<svg class="abs arrow" style="left:800px" width="12" height="16" viewBox="0 0 12 16"><path d="M2 2l6 6-6 6" fill="none" stroke="#1c4a70" stroke-width="3"/></svg>

<section class="abs card slider">
  <div class="slide">
    <div class="slide-photo" role="img" aria-label="Offshore drilling platform standing in open sea under a pale sky"></div>
    <div class="slide-copy">
      <h1>The Business of Drilling Wells</h1>
      <ul>
        <li>Understand and communicate project cost and risk</li>
        <li>Control and reduce expenditure</li>
        <li>Learn and improve performance</li>
      </ul>
    </div>
    <div class="dots"><span></span><span></span><span></span><span></span></div>
  </div>
</section>

<section class="abs card services">
  <h2 class="section-title">Our Services</h2>
  <div class="tiles">
    <div class="tile time">
      <h3>Time &amp; Cost<br>Estimation</h3>
      <div class="visual" role="img" aria-label="Clock resting on a piggy bank"></div>
      <div class="read-more">Read More</div>
    </div>
    <div class="tile dark materials">
      <h3>Materials &amp; Cost<br>Control</h3>
      <div class="visual" role="img" aria-label="Businessman holding floating charts and graphs"></div>
    </div>
    <div class="tile dark lessons">
      <h3>Lessons Learned</h3>
      <div class="visual" role="img" aria-label="Word cloud about learning, training and development"></div>
    </div>
    <div class="tile dark consult">
      <h3>Services &amp; Consulting</h3>
      <div class="visual" role="img" aria-label="Large question marks on a blue background"></div>
    </div>
  </div>
</section>

<h2 class="abs section-title partners-title">Our Partner</h2>
<div class="abs partners">
  <span>Orvadex</span><span>Halvern</span><span>Mesquor</span><span>Brackwell</span><span>KR</span><span>Norquay</span><span>Tellmar</span>
</div>

<section class="abs card info">
  <div class="info-inner">
    <div class="col about">
      <h2>ABOUT US</h2>
      <p>From early phase evaluation through planning, execution and post analysis of wells, we deliver the tools, processes and people required to facilitate major performance improvement and cost savings.</p>
      <p>Our solutions are used in more than 30 countries to support operations ranging from a single well to global deployments with Major Operators.</p>
    </div>
    <div class="col news">
      <h2>LATEST NEWS</h2>
      <p><strong>RiskLine Selected by Brackwell</strong>Brackwell Energy Ltd has selected RiskLine as the solution to provide probabilistic time and cost estimates for its drilling operations.</p>
      <p><strong>CostLine Implementation at Norquay</strong>Norquay selects CostLine to support its materials, logistics &amp; cost management processes.</p>
    </div>
    <div class="col location">
      <h2>Location</h2>
      <p><strong>EUROPE</strong>18 Harlow Terrace<br>Kelbridge<br>KB4 2TN<br>Phone:+44(0)1632 960418<br>Email: eu@corvanisystems.com</p>
      <p><strong>NORTH AMERICA</strong>4100 Lindell Parkway<br>Suite 210<br>Marlow, TX 75001<br>Phone:(555) 014 2278<br>Email: us@corvanisystems.com</p>
    </div>
    <div class="btn-more" style="left:17px">Continue Reading..</div>
    <div class="btn-more" style="left:246px">Continue Reading..</div>
    <div class="btn-more" style="left:474px">Continue Reading..</div>
  </div>
</section>

<div class="abs partner-band"><b>Keystone Partner</b><small>Gold &nbsp;Independent Software Vendor (ISV)</small></div>
<div class="abs touch-band">
  <div class="touch-pill">Get In Touch
    <svg width="18" height="20" viewBox="0 0 18 20"><path d="M4 2l3 4-2 2c1 3 3 5 6 7l2-2 4 3-2 3C8 18 1 11 2 4z" fill="none" stroke="#fff" stroke-width="2"/></svg>
    <svg width="20" height="14" viewBox="0 0 20 14"><rect x="1" y="1" width="18" height="12" fill="none" stroke="#fff" stroke-width="2"/><path d="M1 1l9 7 9-7" fill="none" stroke="#fff" stroke-width="2"/></svg>
    <svg width="14" height="20" viewBox="0 0 14 20"><path d="M7 19S1 11 1 7a6 6 0 0 1 12 0c0 4-6 12-6 12z" fill="none" stroke="#fff" stroke-width="2"/><circle cx="7" cy="7" r="2" fill="#fff"/></svg>
  </div>
</div>

<form class="abs card form-card">
  <div class="form-inner">
    <div class="field" style="left:10px;top:10px;width:140px">First Name</div>
    <div class="field" style="left:158px;top:10px;width:140px">Last Name</div>
    <div class="field" style="left:10px;top:32px;width:140px">Email</div>
    <div class="field" style="left:158px;top:32px;width:140px">Company</div>
    <div class="field" style="left:10px;top:54px;width:220px;height:32px">Message</div>
    <div class="send">SEND</div>
  </div>
</form>

<footer>
  <div class="abs foot-nav"><a class="current" href="#">HOME</a> &nbsp;/ &nbsp;<a href="#">NEWS</a> &nbsp;/ &nbsp;<a href="#">ABOUT US</a> &nbsp;/ &nbsp;<a href="#">SOLUTIONS</a> &nbsp;/ &nbsp;<a href="#">CONTACT US</a></div>
  <div class="abs copyright">All rights reserved 2012 &nbsp; visit our website : www.corvanisystems.com</div>
  <div class="abs social" style="left:731px" aria-label="Social link"></div>
  <div class="abs social" style="left:760px" aria-label="Social link"></div>
</footer>

<div class="band bottom"></div>
</body>
</html>
```